Vesprine Oakville Cabernet Sauvignon-Wine label design

We need a package design for an up market wine brand named, Vesprine. It will be a Cabernet Sauvignon from the Oakville AVA of Napa Valley. We are looking for a stylish modern label that will stand out on a retail shelf. We want the label to be attention grabbing and stylish while presenting an up market luxury brand.

Sick

Requirements
Must have
• Must have the words(in order of importance)
-Vesprine
-Cabernet Sauvignon
-Oakville
-Napa Valley
-2018

Must be designed for a traditional "Bordeaux" style bottle (Bottle specs in uploaded files)
Should not have
• Any images of grapes, vineyards, wine glasses or bottles

```html
<!DOCTYPE html>
<html lang="en">
<head>
<meta charset="utf-8">
<title>Vesprine Cabernet Sauvignon – Label</title>
<link href="https://fonts.googleapis.com/css2?family=Cinzel:wght@400;600&family=Marcellus&family=Allura&display=swap" rel="stylesheet">
<style>
  :root {
    --backdrop: #eeeef2;
    --label-black: #050505;
    --silver: #cfcfd4;
    --silver-light: #e6e6ea;
    --silver-dark: #8e8e94;
  }
  html, body {
    margin: 0;
    padding: 0;
    width: 1200px;
    height: 1200px;
    overflow: hidden;
    background: var(--backdrop);
  }
  .canvas {
    position: relative;
    width: 1200px;
    height: 1200px;
  }
  .label {
    position: absolute;
    left: 240px;
    top: 50px;
    width: 720px;
    height: 1100px;
    overflow: hidden;
    background: var(--label-black);
    box-shadow: 0 10px 40px rgba(0,0,0,0.18);
  }
  .pattern-band {
    position: absolute;
    left: 0;
    width: 720px;
    height: 200px;
    display: block;
  }
  .pattern-band--top { top: 0; }
  .pattern-band--bottom { top: 910px; transform: scaleY(-1); }
  .brand-name {
    position: absolute;
    top: 332px;
    left: 0;
    width: 100%;
    text-align: center;
    font-family: "Marcellus", serif;
    font-weight: 400;
    font-size: 94px;
    letter-spacing: 10px;
    text-indent: 10px;
    color: var(--silver);
    margin: 0;
    line-height: 1;
  }
  .divider {
    position: absolute;
    top: 461px;
    left: 110px;
    width: 500px;
    height: 2px;
    background: var(--silver-dark);
  }
  .varietal {
    position: absolute;
    top: 505px;
    left: 0;
    width: 100%;
    text-align: center;
    font-family: "Allura", cursive;
    font-size: 82px;
    color: var(--silver);
    transform: rotate(-5deg);
    line-height: 1;
    margin: 0;
  }
  .appellation {
    position: absolute;
    top: 788px;
    left: 0;
    width: 100%;
    text-align: center;
    font-family: "Cinzel", serif;
    font-weight: 400;
    font-size: 36px;
    letter-spacing: 3px;
    line-height: 1;
    color: var(--silver-light);
    margin: 0;
  }
  .vintage {
    position: absolute;
    top: 872px;
    left: 0;
    width: 100%;
    text-align: center;
    font-family: "Cinzel", serif;
    font-weight: 600;
    font-size: 32px;
    letter-spacing: 3px;
    line-height: 1;
    color: var(--silver-light);
    margin: 0;
  }
</style>
</head>
<body>
<main class="canvas">
  <section class="label">
    <svg class="pattern-band pattern-band--top" viewBox="0 0 720 200" role="img" aria-label="Silver geometric diamond pattern border">
      <defs>
        <linearGradient id="silverRow" x1="0" y1="0" x2="1" y2="0">
          <stop offset="0" stop-color="#9c9ca2"/>
          <stop offset="0.5" stop-color="#c9c9ce"/>
          <stop offset="1" stop-color="#a4a4aa"/>
        </linearGradient>
        <linearGradient id="silverFade" x1="0" y1="0" x2="0" y2="1">
          <stop offset="0" stop-color="#8e8e94"/>
          <stop offset="1" stop-color="#050505"/>
        </linearGradient>
      </defs>
      <rect x="0" y="24" width="720" height="78" fill="url(#silverRow)"/>
      <line x1="0" y1="106" x2="720" y2="106" stroke="#cfcfd4" stroke-width="1.5"/>
      <line x1="0" y1="112" x2="720" y2="112" stroke="#cfcfd4" stroke-width="1.5"/>
      <rect x="0" y="118" width="720" height="74" fill="url(#silverFade)"/>
    </svg>

    <h1 class="brand-name">VESPRINE</h1>
    <div class="divider"></div>
    <p class="varietal">Cabernet Sauvignon</p>
    <p class="appellation">OAKVILLE, NAPA VALLEY</p>
    <p class="vintage">2018</p>

    <svg class="pattern-band pattern-band--bottom" viewBox="0 0 720 200" role="img" aria-label="Silver geometric diamond pattern border">
      <rect x="0" y="24" width="720" height="78" fill="url(#silverRow)"/>
      <line x1="0" y1="106" x2="720" y2="106" stroke="#cfcfd4" stroke-width="1.5"/>
      <line x1="0" y1="112" x2="720" y2="112" stroke="#cfcfd4" stroke-width="1.5"/>
      <rect x="0" y="118" width="720" height="74" fill="url(#silverFade)"/>
    </svg>
  </section>
</main>
</body>
</html>
```